Business Card Design

Contact Information for Business Card

A vertical business card request- a medium & light gray with silverfern tree logo (logo is attached)

Please use Trebuchet font -- if possible- can we use two different color gray? (See pictures attached below)
Info on the front should be the Silverfern tree logo - on the top of the card, followed by the info ...
Card to read: " " indicated what should be on the card --
Name: " Joan Pelley "
Title : "Partner "
" Office: 202.555.0147 "
" Mobile: 202.555.0182 "

Backside of the card - solid medium color gray color w/ address and small message centered in the card - Trebuchet font
to read:

" 317 B North Linden Avenue, NE "
" Washington, DC 20099 "

Then below address to read:
" Fundraising | Event Planning | Political Consulting "

```html
<!DOCTYPE html>
<html lang="en">
<head>
<meta charset="utf-8">
<title>Silverfern Business Card</title>
<link rel="stylesheet" href="https://fonts.googleapis.com/css2?family=Fira+Sans:wght@300;400;700&family=Fira+Sans+Condensed:wght@700&display=swap">
<style>
  :root {
    --backdrop: #ededed;
    --card-gray: #3e3e3e;
    --card-gray-deep: #333333;
    --silver-light: #d6d6d6;
    --silver-mid: #a9a9a9;
    --ink-white: #f4f4f4;
    --ink-soft: #bdbdbd;
  }
  * { margin: 0; padding: 0; box-sizing: border-box; }
  html, body {
    width: 1200px; height: 801px; overflow: hidden;
    background: var(--backdrop);
    font-family: "Fira Sans", "Trebuchet MS", sans-serif;
  }
  .canvas {
    position: relative; width: 1200px; height: 801px;
    display: flex; justify-content: center; align-items: center; gap: 80px;
  }
  .card {
    position: relative; width: 330px; height: 560px;
    background: var(--card-gray); color: var(--ink-white);
    box-shadow: 0 6px 18px rgba(0,0,0,0.18);
    overflow: hidden;
  }
  .card-back .silver-tab {
    position: absolute; top: 0; left: 0; right: 0; height: 16px;
    background: linear-gradient(90deg, var(--silver-mid), var(--silver-light) 50%, var(--silver-mid));
  }
  .logo {
    display: flex; flex-direction: column; align-items: center;
    font-weight: 300; color: var(--ink-white);
  }
  .logo-mark {
    width: 38px; height: 38px; border-radius: 50%;
    background: var(--ink-white); margin-bottom: 12px;
  }
  .logo-name {
    font-size: 22px; letter-spacing: 4px; line-height: 1;
  }
  .logo-tagline {
    font-size: 8px; letter-spacing: 3px; margin-top: 6px; color: var(--ink-soft);
    text-transform: uppercase;
  }
  .card-back .logo { position: absolute; top: 150px; left: 0; right: 0; }
  .card-back .back-info {
    position: absolute; top: 300px; left: 0; right: 0; text-align: center;
    font-size: 11px; line-height: 1.7; color: var(--ink-soft);
  }
  .card-back .services { margin-top: 10px; font-size: 9.5px; letter-spacing: 0.3px; }

  .card-front .logo { position: absolute; top: 60px; left: 0; right: 0; }
  .identity { position: absolute; top: 205px; left: 42px; }
  .person-name {
    font-family: "Fira Sans Condensed", "Trebuchet MS", sans-serif;
    font-weight: 700; font-size: 30px; letter-spacing: 1px; line-height: 1;
  }
  .person-title { font-size: 10px; letter-spacing: 2px; color: var(--ink-soft); margin-top: 6px; text-transform: uppercase; }
  .contact-list { position: absolute; top: 290px; left: 42px; list-style: none; }
  .contact-item {
    display: flex; align-items: center; gap: 10px;
    font-size: 11px; color: var(--ink-white); height: 26px;
  }
  .contact-icon { width: 16px; height: 16px; flex: none; }
  .silver-band {
    position: absolute; left: 0; right: 0; bottom: 18px; height: 26px;
    background: linear-gradient(90deg, var(--silver-mid), var(--silver-light) 55%, var(--silver-mid));
  }
  .card-front .base-strip {
    position: absolute; left: 0; right: 0; bottom: 0; height: 18px; background: var(--card-gray-deep);
  }
</style>
</head>
<body>
<main class="canvas">
  <section class="card card-back" aria-label="Card back">
    <div class="silver-tab"></div>
    <div class="logo">
      <span class="logo-mark"></span>
      <span class="logo-name">SILVERFERN</span>
      <span class="logo-tagline">Event Group</span>
    </div>
    <div class="back-info">
      <p>317 B North Linden Avenue, NE</p>
      <p>Washington, DC 20099</p>
      <p class="services">Fundraising | Event Planning | Political Consulting</p>
    </div>
  </section>

  <section class="card card-front" aria-label="Card front">
    <div class="logo">
      <span class="logo-mark"></span>
      <span class="logo-name">SILVERFERN</span>
      <span class="logo-tagline">Event Group</span>
    </div>
    <div class="identity">
      <h1 class="person-name">JOAN PELLEY</h1>
      <p class="person-title">Partner</p>
    </div>
    <ul class="contact-list">
      <li class="contact-item">
        <svg class="contact-icon" viewBox="0 0 16 16"><rect width="16" height="16" fill="#f4f4f4"/><path d="M5 3.5h2l1 2.5-1.2 1a6 6 0 0 0 2.2 2.2l1-1.2 2.5 1v2c0 .6-.5 1-1 1A8.5 8.5 0 0 1 4 4.5c0-.5.4-1 1-1z" fill="#3e3e3e"/></svg>
        <span>Office: 202.555.0147</span>
      </li>
      <li class="contact-item">
        <svg class="contact-icon" viewBox="0 0 16 16"><rect width="16" height="16" fill="#f4f4f4"/><rect x="5.5" y="3" width="5" height="10" rx="1" fill="#3e3e3e"/><rect x="6.5" y="4.5" width="3" height="6" fill="#f4f4f4"/></svg>
        <span>Mobile: 202.555.0182</span>
      </li>
      <li class="contact-item">
        <svg class="contact-icon" viewBox="0 0 16 16"><rect width="16" height="16" fill="#f4f4f4"/><rect x="3" y="5" width="10" height="7" fill="#3e3e3e"/><path d="M3 5l5 4 5-4" stroke="#f4f4f4" fill="none"/></svg>
        <span>joan@silverfern.com</span>
      </li>
      <li class="contact-item">
        <svg class="contact-icon" viewBox="0 0 16 16"><rect width="16" height="16" fill="#f4f4f4"/><circle cx="8" cy="8" r="4.5" fill="none" stroke="#3e3e3e" stroke-width="1.2"/><path d="M3.5 8h9M8 3.5c-2 2.5-2 6.5 0 9M8 3.5c2 2.5 2 6.5 0 9" stroke="#3e3e3e" fill="none" stroke-width="0.9"/></svg>
        <span>www.silverfern.com</span>
      </li>
      <li class="contact-item">
        <svg class="contact-icon" viewBox="0 0 16 16"><rect width="16" height="16" fill="#f4f4f4"/><path d="M8 13s-3.5-4-3.5-6.3a3.5 3.5 0 0 1 7 0C11.5 9 8 13 8 13z" fill="#3e3e3e"/><circle cx="8" cy="6.7" r="1.2" fill="#f4f4f4"/></svg>
        <span>Washington, DC 20099</span>
      </li>
    </ul>
    <div class="silver-band"></div>
    <div class="base-strip"></div>
  </section>
</main>
</body>
</html>
```